Brennick Holdings Business Cards

These are professional business cards that are for my family office.
Put fake emails and phone numbers as of now until I finalize those components. This family office controls my families investments, assets, and future. The cards should be professional.
..
.
.
.
I just uploaded another variation of a logo I would like to see as a business card to I am inbeteen which logo to use

Target Market(s)

business

Industry/Entity Type

business

Contact Information for Business Card

Professional, wealth related, finance related.

Requirements
Must have
• Logo

```html
<!DOCTYPE html>
<html lang="en">
<head>
<meta charset="utf-8">
<title>Brennick Holdings Business Cards</title>
<link href="https://fonts.googleapis.com/css2?family=Montserrat:wght@400;500;600;700&display=swap" rel="stylesheet">
<style>
  :root {
    --stage: #2a2b2e;
    --card: #1b2130;
    --card-edge: #242b3d;
    --ink: #ffffff;
    --ink-soft: #c9ccd4;
    --ink-muted: #9aa0ad;
    --accent: #3e4f8f;
    --rule: #8a8f9c;
  }
  * { box-sizing: border-box; margin: 0; padding: 0; }
  html, body { width: 1200px; height: 875px; overflow: hidden; }
  body {
    background: var(--stage);
    font-family: "Montserrat", sans-serif;
    position: relative;
  }
  .card {
    position: absolute;
    top: 283px;
    width: 540px;
    height: 309px;
    background: var(--card);
    border: 1px solid var(--card-edge);
    border-radius: 18px;
    overflow: hidden;
  }
  .card--front { left: 40px; }
  .card--back { left: 620px; }

  /* front */
  .front-ring {
    position: absolute;
    right: 30px;
    top: -40px;
    width: 250px;
    height: 250px;
    border: 4px solid var(--accent);
    border-radius: 50%;
    opacity: 0.7;
  }
  .front-brand {
    position: absolute;
    left: 40px;
    bottom: 44px;
  }
  .wordmark {
    font-weight: 600;
    color: var(--ink);
    text-transform: uppercase;
    letter-spacing: 2px;
  }
  .front-brand .wordmark { font-size: 24px; }
  .front-web {
    margin-top: 6px;
    font-size: 14px;
    font-weight: 600;
    color: var(--ink-muted);
    letter-spacing: 0.5px;
  }

  /* back */
  .back-brand {
    position: absolute;
    left: 28px;
    top: 0;
    width: 220px;
    height: 100%;
    display: flex;
    flex-direction: column;
    align-items: center;
    justify-content: center;
    gap: 18px;
  }
  .brand-dot {
    width: 86px;
    height: 86px;
    border: 3px solid var(--ink);
    border-radius: 50%;
  }
  .back-brand .wordmark { font-size: 17px; }
  .back-rule {
    position: absolute;
    left: 262px;
    top: 70px;
    width: 1px;
    height: 170px;
    background: var(--rule);
  }
  .contact {
    position: absolute;
    left: 282px;
    top: 72px;
    color: var(--ink-soft);
  }
  .contact-name {
    font-size: 19px;
    font-weight: 700;
    color: var(--ink-soft);
  }
  .contact-role {
    font-size: 11px;
    font-weight: 500;
    color: var(--ink-muted);
    margin-bottom: 16px;
  }
  .contact-address {
    font-size: 11px;
    line-height: 1.35;
    margin-bottom: 12px;
  }
  .contact-list { list-style: none; font-size: 11px; }
  .contact-list li {
    display: flex;
    align-items: center;
    gap: 8px;
    line-height: 1.9;
  }
  .contact-list svg { width: 11px; height: 11px; fill: var(--ink-soft); flex: none; }
</style>
</head>
<body>

<section class="card card--front" aria-label="Card front">
  <div class="front-ring"></div>
  <div class="front-brand">
    <div class="wordmark">Brennick Holdings</div>
    <div class="front-web">www.brennickholdings.com</div>
  </div>
</section>

<section class="card card--back" aria-label="Card back">
  <div class="back-brand">
    <div class="brand-dot"></div>
    <div class="wordmark">Brennick Holdings</div>
  </div>
  <div class="back-rule"></div>
  <div class="contact">
    <div class="contact-name">Marcus Ellery</div>
    <div class="contact-role">Owner</div>
    <div class="contact-address">48 Linden Court<br>Fairhaven, NJ 07011 USA</div>
    <ul class="contact-list">
      <li>
        <svg viewBox="0 0 24 24" aria-hidden="true"><path d="M6.6 10.8a15 15 0 0 0 6.6 6.6l2.2-2.2a1 1 0 0 1 1-.25 11.4 11.4 0 0 0 3.6.57 1 1 0 0 1 1 1V20a1 1 0 0 1-1 1A17 17 0 0 1 3 4a1 1 0 0 1 1-1h3.5a1 1 0 0 1 1 1c0 1.25.2 2.45.57 3.6a1 1 0 0 1-.25 1z"/></svg>
        (555)014-2207
      </li>
      <li>
        <svg viewBox="0 0 24 24" aria-hidden="true"><path d="M2 5h20v14H2zm2 2v.4l8 5 8-5V7zm0 2.8V17h16V9.8l-8 5z"/></svg>
        office@brennickholdings.com
      </li>
      <li>
        <svg viewBox="0 0 24 24" aria-hidden="true"><path d="M12 2a10 10 0 1 0 0 20 10 10 0 0 0 0-20zm6.9 6h-3a15 15 0 0 0-1.3-4 8 8 0 0 1 4.3 4zM12 4c.8 1.1 1.5 2.5 1.9 4h-3.8c.4-1.5 1.1-2.9 1.9-4zM4.3 14a8 8 0 0 1 0-4h3.4a16 16 0 0 0 0 4zm.8 2h3a15 15 0 0 0 1.3 4 8 8 0 0 1-4.3-4zm3-8h-3a8 8 0 0 1 4.3-4 15 15 0 0 0-1.3 4zM12 20c-.8-1.1-1.5-2.5-1.9-4h3.8c-.4 1.5-1.1 2.9-1.9 4zm2.3-6H9.7a14 14 0 0 1 0-4h4.6a14 14 0 0 1 0 4zm.3 6a15 15 0 0 0 1.3-4h3a8 8 0 0 1-4.3 4zm1.7-6a16 16 0 0 0 0-4h3.4a8 8 0 0 1 0 4z"/></svg>
        www.brennickholdings.com
      </li>
    </ul>
  </div>
</section>

</body>
</html>
```